6 - 8 'Holistic' Instagram Graphics

Hi there!
We are looking to build up a library of Graphic Templates to use as Instagram & Facebook posts for our Holistic Medi Spa (& 3 other companies eventually)
This competition is for a sample of 6 - 8 designs. For the winner(s), we will make an agreement for a batch order (Looking for 200+ designs in total), and will be looking to make a long term arrangement.
Please find a full job description in the attached Word Document.
Any questions, don't hesitate to ask.
Thanks!
Medical Spa

```html
<!DOCTYPE html>
<html lang="en">
<head>
<meta charset="utf-8">
<title>Holistic Spa Social Post Set</title>
<link rel="stylesheet" href="https://fonts.googleapis.com/css2?family=Oswald:wght@300;400&family=Yellowtail&family=Playfair+Display:wght@700&family=Josefin+Sans:wght@700&display=swap">
<style>
:root{
  --teal:#5a968d;
  --teal-dark:#4d8179;
  --mint:#e3f2f1;
  --peach:#f4c4ae;
  --tan:#d8c3a1;
  --sage:#9fba9a;
  --slate:#a9b7c9;
  --mauve:#d9c6c6;
  --ink:#6b6b6b;
  --frame:#5c5c5c;
  --white:#ffffff;
}
*{margin:0;padding:0;box-sizing:border-box}
html,body{width:1200px;height:735px;overflow:hidden;background:var(--white)}
.canvas{position:relative;width:1200px;height:735px}
.post{position:absolute;width:254px;height:254px;border:1px solid var(--frame);overflow:hidden;background:var(--white)}
.abs{position:absolute}
.label{font-family:"Oswald",sans-serif;font-weight:300;color:var(--ink);letter-spacing:.06em;text-transform:uppercase}
.script{font-family:"Yellowtail",cursive;color:var(--teal);line-height:1}
.serif{font-family:"Playfair Display",serif;font-weight:700;color:var(--teal)}
.photo{position:absolute}
.blob{position:absolute;border-radius:50%}

/* Card 1 */
.post--healthy .photo{left:15px;top:15px;width:130px;height:216px;background:linear-gradient(180deg,#e6e2d8 0%,#c9c0ae 45%,#6f6f66 100%)}
/* Card 2 */
.post--sale{background:var(--mint)}
.post--sale .side{position:absolute;left:144px;top:0;width:110px;height:254px;background:var(--white)}
.offer{position:absolute;left:11px;top:40px;width:124px;height:63px;border:2px solid var(--teal);background:var(--white);text-align:center;font-size:17px;line-height:21px;padding-top:9px}
.btn{position:absolute;left:36px;top:197px;width:70px;height:26px;border:2px solid var(--ink);font-size:10px;text-align:center;line-height:22px;background:var(--peach)}
/* Card 3 */
.post--review .brush{position:absolute;inset:0;background:linear-gradient(160deg,var(--mint) 0%,var(--teal) 18%,var(--mint) 30%,var(--mauve) 55%,var(--slate) 70%,var(--peach) 85%,var(--slate) 100%)}
.review-card{position:absolute;left:44px;top:41px;width:168px;height:168px;background:var(--white);text-align:center;padding:14px 11px 0}
.review-body{font-family:"Oswald",sans-serif;font-weight:300;font-size:4.9px;line-height:9.9px;text-align:justify;color:var(--ink);letter-spacing:.08em;text-transform:uppercase;margin-top:10px}
.review-body .by{float:right;color:#8cc3bb}
.stars{margin-top:7px}
/* Card 4 */
.post--gift .strip{position:absolute;left:0;top:0;width:127px;height:254px;background:var(--mint)}
.gift-head{position:absolute;left:139px;top:40px;font-family:"Josefin Sans",sans-serif;font-weight:700;font-size:28px;line-height:30px;color:var(--teal);letter-spacing:.04em}
.gift-rule{position:absolute;left:140px;top:192px;width:60px;height:1px;background:var(--teal)}
.gift-sub{position:absolute;left:140px;top:199px;font-size:9.5px;line-height:14px;color:var(--teal)}
/* Card 5 */
.post--fact{background:var(--mint)}
.fact-circle{left:0;top:1px;width:252px;height:252px;background:linear-gradient(120deg,var(--peach) 0%,#f6d3c3 70%,#e8ebe3 100%)}
.fact-box{position:absolute;left:50px;top:50px;width:153px;height:154px;border:2px solid var(--white);display:flex;align-items:center;justify-content:center;text-align:center;font-size:16.5px;line-height:21px}
.fact-tag{position:absolute;left:50px;top:204px;width:92px;height:23px;border:2px solid var(--white);color:var(--white);font-size:9.5px;line-height:19px;padding-left:4px}
/* Card 6 */
.post--breathe{background:var(--mint)}
.breathe-text{position:absolute;left:166px;top:74px;font-size:17px;line-height:21px}
/* Card 7 */
.post--skin .photo{left:128px;top:0;width:126px;height:254px;background:linear-gradient(180deg,#ecebea 0%,#c89a7c 45%,#8a5a40 100%)}
.skin-box{position:absolute;left:42px;top:47px;width:170px;height:168px;background:var(--white);display:flex;align-items:center;justify-content:center;text-align:center;font-size:16.5px;line-height:21px;padding:0 8px}
/* Card 8 */
.post--giveaway .terrazzo{position:absolute;inset:0;background:radial-gradient(circle at 12% 10%,rgba(90,150,141,.35),transparent 18%),radial-gradient(circle at 85% 8%,rgba(159,186,154,.4),transparent 18%),radial-gradient(circle at 90% 60%,rgba(216,195,161,.4),transparent 16%),radial-gradient(circle at 6% 55%,rgba(244,196,174,.45),transparent 16%),var(--white)}
.give-band{position:absolute;left:52px;top:74px;width:150px;height:10px;background:var(--peach)}
.give-tag{position:absolute;left:80px;top:110px;width:99px;height:25px;background:var(--mint);border-bottom:2px solid var(--teal);color:var(--teal);font-size:10px;line-height:24px;text-align:center;z-index:2}
.post--giveaway .photo{left:22px;top:116px;width:212px;height:113px;background:linear-gradient(90deg,#e7e1d6 0%,#c79c80 50%,#6f8f68 100%)}
</style>
</head>
<body>
<main class="canvas">

  <!-- Healthy mind -->
  <section class="post post--healthy" style="left:38px;top:94px">
    <div class="blob" style="left:170px;top:-40px;width:120px;height:110px;background:var(--mint)"></div>
    <div class="blob" style="left:205px;top:150px;width:70px;height:90px;background:var(--peach)"></div>
    <div class="abs" style="left:0;top:0;width:16px;height:10px;background:var(--tan)"></div>
    <div class="photo" role="img" aria-label="Woman sitting by the sea at sunrise"></div>
    <p class="label abs" style="left:103px;top:22px;font-size:9.5px">The key to a</p>
    <p class="script abs" style="left:100px;top:33px;font-size:44px">Healthy</p>
    <p class="label abs" style="left:150px;top:80px;font-size:9.5px">Lifestyle</p>
    <p class="label abs" style="left:150px;top:96px;font-size:9.5px">is having a healthy</p>
    <p class="script abs" style="left:138px;top:108px;font-size:48px">Mind.</p>
  </section>

  <!-- Sale -->
  <section class="post post--sale" style="left:327px;top:94px">
    <div class="side"></div>
    <div class="blob" style="left:193px;top:-16px;width:46px;height:46px;background:var(--tan)"></div>
    <div class="blob" style="left:145px;top:20px;width:46px;height:46px;border:4px solid var(--teal);background:transparent"></div>
    <div class="blob" style="left:20px;top:212px;width:60px;height:38px;background:var(--peach)"></div>
    <div class="blob" style="left:78px;top:165px;width:12px;height:10px;background:var(--peach)"></div>
    <div class="blob" style="left:110px;top:130px;width:30px;height:130px;border:3px solid var(--tan);background:transparent"></div>
    <p class="label abs" style="left:45px;top:20px;width:95px;text-align:center;font-size:9.5px">Only today</p>
    <div class="offer serif">20% OFF<br>everything!</div>
    <div class="btn label">Shop now!</div>
    <div class="photo" role="img" aria-label="Woman receiving a relaxing back massage" style="left:153px;top:44px;width:89px;height:191px;background:linear-gradient(180deg,#e5c3a7 0%,#c78d6c 55%,#f0ede9 100%)"></div>
    <div class="abs" style="left:236px;top:14px;width:3px;height:64px;background:var(--teal);transform:rotate(18deg)"></div>
  </section>

  <!-- Testimonial -->
  <section class="post post--review" style="left:616px;top:94px">
    <div class="brush" role="img" aria-label="Painted brush strokes in teal, blue, mauve and peach"></div>
    <div class="review-card">
      <p class="label" style="font-size:8px;font-weight:400">Testimonial</p>
      <p class="review-body">It's my first time to go to Willow Spa. But I received a very welcoming treatment from ma'am Elena and she did a very professional way of telling me my treatment, and I will go and continue to support their business, and also I will recommend Willow Spa to my friend who want to have their skin treated. Well done Willow Spa. I will see you in a month time. Thank you for the nice treatment. <span class="by">- Clara Moss</span></p>
      <svg class="stars" width="78" height="13" viewBox="0 0 78 13" aria-label="Five stars">
        <g fill="#f5e8a8" stroke="#c9b66a" stroke-width=".6">
          <polygon points="6.5,0.5 8.3,4.6 12.6,4.8 9.2,7.6 10.3,12 6.5,9.6 2.7,12 3.8,7.6 0.4,4.8 4.7,4.6"/>
          <polygon transform="translate(16 0)" points="6.5,0.5 8.3,4.6 12.6,4.8 9.2,7.6 10.3,12 6.5,9.6 2.7,12 3.8,7.6 0.4,4.8 4.7,4.6"/>
          <polygon transform="translate(32 0)" points="6.5,0.5 8.3,4.6 12.6,4.8 9.2,7.6 10.3,12 6.5,9.6 2.7,12 3.8,7.6 0.4,4.8 4.7,4.6"/>
          <polygon transform="translate(48 0)" points="6.5,0.5 8.3,4.6 12.6,4.8 9.2,7.6 10.3,12 6.5,9.6 2.7,12 3.8,7.6 0.4,4.8 4.7,4.6"/>
          <polygon transform="translate(64 0)" points="6.5,0.5 8.3,4.6 12.6,4.8 9.2,7.6 10.3,12 6.5,9.6 2.7,12 3.8,7.6 0.4,4.8 4.7,4.6"/>
        </g>
      </svg>
    </div>
    <svg class="abs" style="left:48px;top:24px" width="32" height="26" viewBox="0 0 32 26" aria-hidden="true">
      <path d="M4 0h9L9 12h5v14H2V12z M20 0h9l-4 12h5v14H18V12z" fill="var(--peach)"/>
    </svg>
    <svg class="abs" style="left:95px;top:208px" width="20" height="14" viewBox="0 0 20 14" aria-hidden="true"><path d="M0 0h20L4 14z" fill="var(--white)"/></svg>
  </section>

  <!-- Gift -->
  <section class="post post--gift" style="left:907px;top:94px">
    <div class="strip"></div>
    <div class="abs" style="left:26px;top:28px;width:8px;height:34px;background:var(--teal);border-radius:3px"></div>
    <div class="photo" role="img" aria-label="Fresh green salad with croutons and dressing" style="left:18px;top:44px;width:89px;height:192px;background:linear-gradient(160deg,#cfe3c8 0%,#5f9a4c 40%,#2f6b3a 70%,#d8c7a6 100%)"></div>
    <h2 class="gift-head">WE<br>HAVE<br>A GIFT<br>FOR<br>YOU!</h2>
    <div class="gift-rule"></div>
    <p class="gift-sub label">Enjoy a free<br>ayurvedic recipe<br>book &amp; meal plan</p>
  </section>

  <!-- Fun fact -->
  <section class="post post--fact" style="left:38px;top:384px">
    <svg class="abs" style="left:0;top:0" width="254" height="254" viewBox="0 0 254 254" aria-hidden="true">
      <polygon points="0,0 40,0 0,40" fill="var(--peach)"/>
      <polygon points="254,214 254,254 214,254" fill="var(--peach)"/>
    </svg>
    <div class="blob fact-circle"></div>
    <p class="label abs" style="left:0;top:27px;width:254px;text-align:center;color:var(--white);font-size:9.5px">Did you know...</p>
    <div class="fact-box serif">that EMS Body Sculpting is equivalent to 16 weeks HIT Training?</div>
    <div class="fact-tag label">Fun fact Monday</div>
  </section>

  <!-- Breathe -->
  <section class="post post--breathe" style="left:327px;top:384px">
    <div class="abs" style="left:0;top:56px;width:160px;height:198px;background:var(--white)"></div>
    <p class="label abs" style="left:14px;top:12px;font-size:9.5px">Meditation is</p>
    <div class="abs" style="left:0;top:27px;width:95px;height:1px;background:var(--peach)"></div>
    <p class="label abs" style="left:14px;top:33px;font-size:9.5px">Hanging out with your soul</p>
    <div class="abs" style="left:0;top:48px;width:158px;height:1px;background:var(--peach)"></div>
    <div class="photo" role="img" aria-label="Woman meditating cross-legged by the sea" style="left:9px;top:66px;width:133px;height:171px;background:linear-gradient(180deg,#e9d9c3 0%,#d6b08e 45%,#8a6a52 100%)"></div>
    <p class="breathe-text serif">slow<br>down<br>-<br>just<br>breathe...</p>
  </section>

  <!-- Skincare -->
  <section class="post post--skin" style="left:616px;top:384px">
    <div class="photo" role="img" aria-label="Woman with headband cleansing her skin with a cotton pad"></div>
    <div class="skin-box serif">When did you last consider your skincare routine?</div>
  </section>

  <!-- Giveaway -->
  <section class="post post--giveaway" style="left:907px;top:384px">
    <div class="terrazzo" role="img" aria-label="Terrazzo pattern of teal, sage, tan and peach pebbles"></div>
    <p class="script abs" style="left:0;top:30px;width:254px;text-align:center;font-size:44px">Giveaway</p>
    <div class="give-band"></div>
    <p class="abs" style="left:0;top:74px;width:254px;text-align:center;font-family:'Josefin Sans',sans-serif;font-weight:700;font-size:8px;letter-spacing:.08em;color:var(--teal)">SHARE THIS POST WITH</p>
    <p class="abs" style="left:0;top:88px;width:254px;text-align:center;font-family:'Josefin Sans',sans-serif;font-weight:700;font-size:8px;letter-spacing:.08em;color:var(--teal)">A FRIEND &amp; WIN A</p>
    <div class="give-tag label">Free treatment</div>
    <div class="photo" role="img" aria-label="Woman relaxing during a head massage treatment"></div>
  </section>

</main>
</body>
</html>
```